NEW Website DESIGN for Glass & Solid Surfaces Company

Brand New website, contemporary, clean, visual (images), not busy. ATTACHED IS OUR LOG THAT YOU MUST USE.

The company is called Brightwell Panes & Stoneworks (BrightwellPS)
www.brightwellps.com
The website should be www.brightwellpns.com
one page for glass one page for solid surfaces www.brightwellpanesplashes.co.uk
www.brightwellstoneworkss.co.uk

Target Market(s)

Hotels, Commercial projects, Small focus on residential

Industry/Entity Type

Construction

Number of Pages Required

5+ page

Font styles to use
Sans Serif

Requirements
Must have
• COLOURS AS PER OUR LOGO - WHITE/YELLOW/GREY - WHITE BACK GROUND
• CLEAR SIMPLE NAVIGATION - MODER CLEAN CUT - DESIGN FEEL
• LATEST NAVIGATION FOR IMAGES and text to include per project details
• WORK/PROJECT AREA - NEWS AREA - TEAM AREA/ABOUT US/CONTACT US
• NEW PAGEwww.brightwellpanesplashes.co.uk - NEW PAGE www.brightwellstoneworkss.co.uk
• PLEASE COPY THIS TYPE OF TEMPALTE
• https://www.harlowmead.co.uk/project/grand-halls/
• MOBILE READY
• WORDPRESS
• MODERN IMAGES INCLUDING VELMARA KESTRIN AND GLASS PROJECTS
Nice to have
• NEW DESIGN MODER FRESH
• WEBSITES I LIKE THE TEMPLATE SHOULD BE LIKE THE WEBSITE BELOW
• https://www.harlowmead.co.uk/
Should not have
• NOT Old fashion template, not busy NAVIGATION
• NO BLACK
• NO DARK GREYS
• NOT LOTS OF YELLOW
• RESDENTIAL IMAGES

```html
<!DOCTYPE html>
<html lang="en">
<head>
<meta charset="utf-8">
<title>Brightwell Panes &amp; Stoneworks</title>
<link href="https://fonts.googleapis.com/css2?family=Questrial&family=Lato:wght@400;700&display=swap" rel="stylesheet">
<style>
:root{
  --yellow:#f3e62a;
  --grey:#8c8c8c;
  --grey-mid:#a6a6a6;
  --grey-light:#ececec;
  --grey-soft:#f4f4f4;
  --text:#555555;
  --text-soft:#777777;
  --white:#ffffff;
}
*{margin:0;padding:0;box-sizing:border-box}
html,body{width:1200px;height:2941px;overflow:hidden;background:var(--white)}
body{position:relative;font-family:"Lato",sans-serif;color:var(--text)}
.abs{position:absolute}
h1,h2,h3,.heading{font-family:"Questrial",sans-serif;font-weight:400}

/* sidebar */
.sidebar{left:0;top:0;width:247px;height:2941px;background:var(--white);border-right:1px solid #e6e6e6}
.brand{left:0;top:38px;width:247px;text-align:center}
.brand-mark{width:70px;height:70px;border-radius:50%;background:var(--grey);margin:0 auto 12px}
.brand-name{font-family:"Questrial",sans-serif;font-size:14px;color:var(--text);font-weight:400}
.nav{left:60px;top:182px;width:127px;list-style:none}
.nav li{height:43px;line-height:38px;text-align:center;font-size:12px;color:var(--text);border-bottom:1px solid #ececec}
.nav li:last-child{border-bottom:none}
.nav li.active{color:#333}
.contact-side{left:0;width:247px;text-align:center;font-size:10px;color:var(--text)}
.contact-side b{display:block;font-size:8px;letter-spacing:.5px;margin-bottom:3px}
.socials{left:52px;top:562px;display:flex;gap:11px}
.socials span{width:26px;height:26px;border:1.5px solid var(--grey);border-radius:50%}

/* hero */
.hero{left:247px;top:0;width:953px;height:612px;background:linear-gradient(100deg,#4b3626 0%,#8a6a4a 22%,#cfc4b8 45%,#eeeae6 65%,#d6cfc7 85%,#a99b8c 100%)}
.hero-title{left:247px;top:255px;width:953px;text-align:center;color:var(--white);font-size:34px;font-family:"Questrial",sans-serif;letter-spacing:.3px;font-weight:700}
.btn{display:flex;align-items:center;height:32px;border-radius:16px;padding:0 18px 0 4px;font-size:10px;font-weight:700;letter-spacing:.5px}
.btn i{width:26px;height:26px;border-radius:50%;margin-right:12px;display:block}
.btn-light{background:var(--white);color:var(--text)}
.btn-light i{background:var(--grey)}
.btn-grey{background:var(--grey);color:var(--white)}
.btn-grey i{background:var(--white);border:3px solid var(--yellow)}

/* division cards */
.division{top:572px;height:275px;background:var(--white);padding:5px;box-shadow:0 2px 10px rgba(0,0,0,.2)}
.division .photo{width:100%;height:100%}
.division .label{position:absolute;left:18px;bottom:30px;transform:rotate(-90deg);transform-origin:left bottom;color:var(--white);font-size:13px;white-space:nowrap}
.division .visit{position:absolute;right:22px;bottom:20px;color:var(--yellow);font-size:10px;font-weight:700;display:flex;align-items:center;gap:8px}

/* section heads */
.section-title{text-align:center;font-size:26px;color:var(--text)}
.divider{display:flex;align-items:center;justify-content:center;gap:6px;margin-top:8px}
.divider span{width:58px;height:1px;background:#d4d4d4}
.divider i{width:9px;height:9px;border-radius:50%;background:var(--grey-mid)}

.about-text{left:330px;top:957px;width:786px;text-align:center;font-size:10px;line-height:21px;color:var(--text)}

/* project */
.project-panel{left:247px;top:1143px;width:394px;height:360px;background:linear-gradient(135deg,#f0f0f0,#e8e8e8 50%,#f3f3f3)}
.project-panel h2{font-size:27px;color:var(--text);margin:52px 0 0 84px}
.project-panel h3{font-family:"Lato",sans-serif;font-weight:700;font-size:12px;margin:46px 0 0 84px;color:var(--text)}
.project-panel p{font-size:10px;line-height:21px;margin:13px 0 0 84px;width:270px}
.project-img{top:1143px;height:360px}
.project-caption{left:776px;top:1455px;color:var(--white);font-size:12px;text-align:right}
.project-caption small{display:block;color:var(--yellow);font-size:10px;margin-top:2px}

/* team */
.member{top:1633px;width:164px;text-align:center}
.avatar{width:164px;height:164px;border-radius:50%;border:7px solid var(--grey-mid);padding:5px;background:var(--white)}
.avatar.active{border-color:var(--yellow)}
.avatar div{width:100%;height:100%;border-radius:50%}
.member h4{font-family:"Questrial",sans-serif;font-weight:400;font-size:13px;margin-top:18px;color:var(--text)}
.member p{font-size:10px;color:var(--text-soft);margin-top:4px}
.dots{left:705px;top:1872px;display:flex;gap:6px}
.dots i{width:6px;height:6px;border-radius:50%;background:#bdbdbd}
.dots i.on{background:var(--yellow)}

/* news */
.news-band{left:247px;top:1927px;width:953px;height:478px;background:var(--grey-soft)}
.news-card{top:2048px;width:230px;height:298px;background:var(--white);box-shadow:0 1px 4px rgba(0,0,0,.08);text-align:center}
.news-card .photo{height:147px;border-bottom:3px solid var(--grey-mid)}
.news-date{position:absolute;left:96px;top:128px;width:38px;height:38px;border-radius:50%;background:var(--yellow);border:3px solid var(--white);font-size:8px;line-height:11px;padding-top:6px;color:var(--text);font-weight:700}
.news-card h4{font-family:"Questrial",sans-serif;font-weight:700;font-size:12px;margin:34px 12px 0;color:var(--text)}
.news-card p{font-size:9px;line-height:19px;margin:8px 22px 0;color:var(--text)}

/* clients */
.clients{left:333px;top:2462px;width:790px;height:64px;display:flex;align-items:center;justify-content:space-between}
.client{font-family:"Questrial",sans-serif;color:var(--grey);font-size:22px;display:flex;align-items:center;gap:8px}
.client.box{background:var(--white);box-shadow:0 1px 6px rgba(0,0,0,.18);padding:14px 22px;font-size:14px}
.client .dot{width:26px;height:26px;border-radius:50%;background:var(--grey-mid)}

/* newsletter + footer */
.footer{left:247px;top:2610px;width:953px;height:331px;background:var(--grey-soft)}
.cta{left:333px;top:2571px;width:837px;height:71px;background:var(--grey);display:flex;align-items:center;padding:0 20px}
.cta h3{color:var(--white);font-size:19px;margin-right:34px}
.field{background:var(--white);height:26px;font-size:9px;color:var(--text-soft);padding:7px 8px}
.cta .field{width:205px;margin-right:10px}
.cta .send{width:92px;height:26px;background:var(--yellow);color:var(--text);font-size:10px;font-weight:700;text-align:center;line-height:26px;margin-left:4px}
.cta-tab{top:2571px;width:0;height:0;border-bottom:20px solid #6e6e6e}

.foot-title{font-family:"Questrial",sans-serif;font-size:18px;color:var(--text)}
.form .field{position:absolute}
.submit{left:333px;top:2844px;width:94px;height:26px;border-radius:13px;background:var(--grey);color:var(--white);font-size:9px;font-weight:700;text-align:center;line-height:26px}
.contact-row{left:700px;display:flex;gap:14px;font-size:9px;line-height:15px;color:var(--text)}
.contact-row svg{flex:none}
.foot-brand{left:940px;top:2688px;width:170px;text-align:center}
.foot-brand .brand-mark{width:74px;height:74px;margin-bottom:10px}
.foot-brand .brand-name{font-size:13px}
.foot-social{display:flex;justify-content:center;gap:6px;margin-top:10px}
.foot-social i{width:18px;height:18px;border-radius:50%;background:var(--grey)}
.copyright{left:333px;top:2898px;width:780px;border-top:1px solid #dcdcdc;padding-top:16px;text-align:center;font-size:8px;letter-spacing:.6px;color:var(--text-soft)}
</style>
</head>
<body>

<!-- Sidebar -->
<aside class="abs sidebar">
  <div class="abs brand">
    <div class="brand-mark"></div>
    <div class="brand-name">Brightwell Panes &amp; Stoneworks</div>
  </div>
  <ul class="abs nav">
    <li class="active">Project</li>
    <li>News</li>
    <li>Team</li>
    <li>About Us</li>
    <li>Contact Us</li>
  </ul>
  <div class="abs contact-side" style="top:448px"><b>CALL US</b>+44 (0)1632 960 418</div>
  <div class="abs" style="left:20px;top:488px;width:207px;height:1px;background:#ececec"></div>
  <div class="abs contact-side" style="top:500px"><b>MAIL US</b>sales@brightwellpanesplashes.co.uk</div>
  <div class="abs socials"><span></span><span></span><span></span><span></span></div>
</aside>

<!-- Hero -->
<section class="abs hero" role="img" aria-label="Photo of a bright open-plan office with glass partitions, timber floor and pendant lights"></section>
<h1 class="abs hero-title">Glass Splashbacks Designed By You</h1>
<div class="abs btn btn-light" style="left:618px;top:316px">
  <i></i>GET IN TOUCH FOR A QUOTE
</div>

<!-- Divisions -->
<a class="abs division" style="left:333px;width:370px">
  <div class="photo" role="img" aria-label="Photo of a high-rise apartment with glass kitchen island and city view" style="background:linear-gradient(160deg,#9eb3c4 0%,#d8d4cc 45%,#8a7a68 80%,#5a4a3a 100%)"></div>
  <span class="label">Brightwell Panes</span>
  <span class="visit">VISIT NOW
    <svg width="20" height="8" viewBox="0 0 20 8"><path d="M0 4h18M14 1l4 3-4 3" stroke="#f3e62a" stroke-width="1.2" fill="none"/></svg></span>
</a>
<a class="abs division" style="left:741px;width:372px">
  <div class="photo" role="img" aria-label="Photo of a white kitchen with solid surface worktops" style="background:linear-gradient(160deg,#e8e8e6 0%,#f4f4f2 40%,#c9c6c1 75%,#8c8882 100%)"></div>
  <span class="label">Stoneworks</span>
  <span class="visit">VISIT NOW
    <svg width="20" height="8" viewBox="0 0 20 8"><path d="M0 4h18M14 1l4 3-4 3" stroke="#f3e62a" stroke-width="1.2" fill="none"/></svg></span>
</a>

<!-- About -->
<section class="abs" style="left:247px;top:896px;width:953px">
  <h2 class="section-title">About Us</h2>
  <div class="divider"><span></span><i></i><span></span></div>
</section>
<p class="abs about-text">We design, cut and fit made-to-measure glass splashbacks and solid surface worktops for hotels, restaurants and commercial spaces across the region. Every panel is templated on site, finished in our own workshop and installed by a trained team. From a single bar counter to a full hotel refurbishment, we work to your programme, your budget and your finish, and we stay on hand long after the final fitting. Ask us about colour matching, samples and site surveys.</p>
<div class="abs btn btn-grey" style="left:661px;top:1056px"><i></i>READ MORE</div>

<!-- Latest project -->
<section class="abs project-panel">
  <h2>Latest Project</h2>
  <h3>Brightwell Panes / Brightwell Stoneworks</h3>
  <p>Toughened glass and seamless worktops fitted in a city hotel, from guest bathrooms to the lobby bar.</p>
  <div class="btn btn-grey" style="position:absolute;left:84px;top:240px;width:128px"><i></i>VIEW ALL</div>
</section>
<div class="abs project-img" style="left:641px;width:245px;background:linear-gradient(170deg,#cfd3d2 0%,#e9e7e3 40%,#6b5f55 70%,#8e8a86 100%)" role="img" aria-label="Photo of a hotel bedroom with glass walls"></div>
<div class="abs project-img" style="left:888px;width:171px;background:linear-gradient(180deg,#f1f1ef 0%,#dcdcda 55%,#b9b7b3 100%)" role="img" aria-label="Photo of a bathroom with glass shower screen"></div>
<div class="abs project-img" style="left:1061px;width:139px;background:linear-gradient(180deg,#dfe4e6 0%,#f2f2f0 45%,#9a9a98 100%)" role="img" aria-label="Photo of an office with glass partitions"></div>
<div class="abs project-caption">GLASS ROOM<small>View Project</small></div>

<!-- Team -->
<section class="abs" style="left:247px;top:1557px;width:953px">
  <h2 class="section-title">Our Team</h2>
  <div class="divider"><span></span><i></i><span></span></div>
</section>
<div class="abs member" style="left:335px">
  <div class="avatar"><div role="img" aria-label="Portrait of the founder" style="background:linear-gradient(180deg,#c7ccd2,#4e5866)"></div></div>
  <h4>Maren Hollis</h4><p>Founder &amp; CEO</p>
</div>
<div class="abs member" style="left:540px">
  <div class="avatar active"><div role="img" aria-label="Portrait of the managing director" style="background:linear-gradient(180deg,#e4e6e8,#7d8fa8)"></div></div>
  <h4>Tobias Wren</h4><p>Managing Director</p>
</div>
<div class="abs member" style="left:746px">
  <div class="avatar"><div role="img" aria-label="Portrait of the project manager" style="background:linear-gradient(180deg,#c9ced4,#2f3a4e)"></div></div>
  <h4>Adrian Calloway</h4><p>Project Manager</p>
</div>
<div class="abs member" style="left:953px">
  <div class="avatar"><div role="img" aria-label="Portrait of the general manager" style="background:linear-gradient(180deg,#e9e6e2,#3a3230)"></div></div>
  <h4>Priya Daventry</h4><p>General Manager</p>
</div>
<div class="abs dots"><i></i><i class="on"></i><i></i></div>

<!-- News -->
<section class="abs news-band"></section>
<section class="abs" style="left:247px;top:1965px;width:953px">
  <h2 class="section-title">Latest News</h2>
  <div class="divider"><span></span><i></i><span></span></div>
</section>
<article class="abs news-card" style="left:333px">
  <div class="photo" role="img" aria-label="Photo of a café counter with glass worktops" style="background:linear-gradient(180deg,#d8d6d2,#6e655c)"></div>
  <div class="news-date">06<br>Aug</div>
  <h4>Glass Worktops in record time!</h4>
  <p>On our Throwback Thursday posts, we like to remember some of the great work we've done over the years! Back in 2016, we did these absolutely...</p>
</article>
<article class="abs news-card" style="left:608px">
  <div class="photo" role="img" aria-label="Photo of a hotel room with purple glass splashback" style="background:linear-gradient(180deg,#8e7aa8,#e2e0e6 60%,#c4c2c6)"></div>
  <div class="news-date">06<br>Aug</div>
  <h4>Bathroom glass splashbacks at.</h4>
  <p>We've been busy here at Brightwell Panes &amp; Splashes! We've been doing some fun residential jobs for lovely clients - our glass splashbacks are...</p>
</article>
<article class="abs news-card" style="left:882px">
  <div class="photo" role="img" aria-label="Photo of a hotel swimming pool with glass screens" style="background:linear-gradient(180deg,#cfd8dc,#4aa6d6 65%,#2a79b0)"></div>
  <div class="news-date">06<br>Aug</div>
  <h4>Harrowgate Lodge Inn – beautiful</h4>
  <p>Tempting though it was to take a dip in the pool, we remained consummate professionals when working at this lovely spa at the Harrowgate Lodge Inn!</p>
</article>
<div class="abs btn btn-grey" style="left:667px;top:2388px;padding-right:22px"><i></i>VIEW ALL</div>

<!-- Clients -->
<div class="abs clients">
  <span class="client" style="font-size:16px"><span class="dot"></span>Lindqvist</span>
  <span class="client box"><span class="dot"></span>Marrow Café</span>
  <span class="client" style="font-size:26px">the fairley</span>
  <span class="client" style="font-size:22px">QRT</span>
  <span class="client" style="font-size:26px">Ostrander</span>
</div>

<!-- Footer -->
<section class="abs footer"></section>
<div class="abs cta-tab" style="left:318px;border-left:15px solid transparent"></div>
<div class="abs cta-tab" style="left:1170px;border-right:15px solid transparent"></div>
<div class="abs cta">
  <h3 class="heading">Want To Know More?</h3>
  <div class="field">Enter Name</div>
  <div class="field">Enter Email</div>
  <div class="send">SEND</div>
</div>

<h3 class="abs foot-title" style="left:333px;top:2680px">Get In Touch</h3>
<div class="form">
  <div class="field" style="left:333px;top:2714px;width:147px;height:24px">Name</div>
  <div class="field" style="left:489px;top:2714px;width:147px;height:24px">Phone</div>
  <div class="field" style="left:333px;top:2746px;width:303px;height:24px">Email</div>
  <div class="field" style="left:333px;top:2778px;width:303px;height:54px">Message</div>
</div>
<div class="abs submit">Submit Now</div>

<h3 class="abs foot-title" style="left:700px;top:2680px">Contact Me</h3>
<div class="abs contact-row" style="top:2718px">
  <svg width="10" height="14" viewBox="0 0 10 14"><path d="M5 0a5 5 0 0 1 5 5c0 4-5 9-5 9S0 9 0 5a5 5 0 0 1 5-5z" fill="#8c8c8c"/><circle cx="5" cy="5" r="2" fill="#f4f4f4"/></svg>
  <span>HEAD OFFICE<br>Unit 4 Millbrook Court, Fenwick Lane<br>Oxbury OX9 2LT</span>
</div>
<div class="abs contact-row" style="top:2776px">
  <svg width="11" height="11" viewBox="0 0 11 11"><path d="M2 0l2 2.5-1.2 1.5c.6 1.6 2 3 3.6 3.6L8 6.4 11 8.5 9.5 11C4.5 11 0 6.5 0 1.5z" fill="#8c8c8c"/></svg>
  <span style="font-size:11px">+44 (0)1632 960 418</span>
</div>
<div class="abs contact-row" style="top:2808px">
  <svg width="11" height="9" viewBox="0 0 11 9"><rect width="11" height="9" fill="#8c8c8c"/><path d="M0 0l5.5 5L11 0" stroke="#f4f4f4" fill="none"/></svg>
  <span>sales@brightwellpanesplashes.co.uk</span>
</div>
<div class="abs" style="left:925px;top:2700px;width:1px;height:140px;background:#dcdcdc"></div>
<div class="abs foot-brand">
  <div class="brand-mark"></div>
  <div class="brand-name">Brightwell Panes &amp; Stoneworks</div>
  <div class="foot-social"><i></i><i></i><i></i><i></i></div>
</div>
<div class="abs copyright">© 2018 BRIGHTWELLPS. ALL RIGHTS RESERVED.</div>

</body>
</html>
```